Business card design for international hub site

I need a business card design with the logo attached. Although the site is for the teenage audience (it is about the high school graduation ball, the Prom), the business card is for professional use to be given to professional contacts (B2B), such as suppliers and partners, so it needs to look professional (but also girly, glamours and clean).

Target Market(s)

B2B

Industry/Entity Type

Media

Colors
eea4c8
f9d9e8
e667a6
9d9d9d
1b1b1b

Requirements
Must have
• Space for Name, Tile, Address, Phone, email and website.
Should not have
• Photo

```html
<!DOCTYPE html>
<html lang="en">
<head>
<meta charset="utf-8">
<title>Gala Glow – Business Card</title>
<link rel="stylesheet" href="https://fonts.googleapis.com/css2?family=EB+Garamond:wght@400;600&display=swap">
<style>
  :root {
    --pink: #e667a6;
    --pink-soft: #eea4c8;
    --grey: #9d9d9d;
    --ink: #1b1b1b;
    --slate: #3e3e3e;
    --paper: #ffffff;
    --stage: #d6d6d6;
  }
  * { box-sizing: border-box; margin: 0; padding: 0; }
  html, body { width: 1200px; height: 1200px; overflow: hidden; }
  body {
    background: radial-gradient(circle at 50% 45%, #ececec 0%, var(--stage) 70%, #bdbdbd 100%);
    font-family: "EB Garamond", Georgia, serif;
    color: var(--ink);
  }
  .sheet {
    width: 1200px; height: 1200px;
    display: flex; flex-direction: column; align-items: center; justify-content: center;
    gap: 56px;
  }
  .card {
    position: relative;
    width: 945px; height: 540px;
    overflow: hidden;
    box-shadow: 0 10px 30px rgba(0,0,0,.22);
  }
  .card--front { background: var(--paper); }
  .card--back { background: var(--slate); }
  .card__band { position: absolute; left: 0; bottom: 0; width: 100%; height: 200px; }

  .brand {
    position: absolute;
    font-weight: 400;
    color: var(--pink);
    line-height: 1;
    letter-spacing: 1px;
    white-space: nowrap;
  }
  .card--front .brand { left: 70px; top: 120px; font-size: 112px; }
  .card--back .brand { left: 0; right: 0; top: 170px; text-align: center; font-size: 140px; }

  .address {
    position: absolute; left: 76px; top: 372px;
    font-size: 27px; line-height: 1.25;
  }
  .person {
    position: absolute; right: 48px; top: 135px; text-align: right;
  }
  .person__name { font-size: 36px; font-weight: 600; line-height: 1.1; }
  .person__title { font-size: 22px; font-style: italic; }

  .contacts {
    position: absolute; right: 48px; top: 252px;
    list-style: none; text-align: right;
    font-size: 25px; line-height: 37px;
  }
  .contacts li { display: flex; align-items: center; justify-content: flex-end; gap: 10px; }
  .contacts svg { width: 24px; height: 24px; flex: none; }

  .website {
    position: absolute; right: 30px; bottom: 16px;
    color: var(--paper); font-size: 27px; font-weight: 600;
  }
</style>
</head>
<body>
<main class="sheet">

  <section class="card card--front" aria-label="Business card front">
    <svg class="card__band" viewBox="0 0 945 200" preserveAspectRatio="none" aria-hidden="true">
      <path d="M380 130 C620 120 820 80 945 20 L945 60 C800 110 600 132 380 132 Z" fill="var(--grey)"/>
      <path d="M0 132 C350 132 700 120 945 55 L945 200 L0 200 Z" fill="var(--pink)"/>
    </svg>

    <div class="brand">Gala Glow</div>

    <p class="address">Unit, Street,<br>City, State, Zip</p>

    <div class="person">
      <p class="person__name">Name Here</p>
      <p class="person__title">Title</p>
    </div>

    <ul class="contacts">
      <li>(000) 000-0000
        <svg viewBox="0 0 24 24" aria-label="Mobile"><circle cx="12" cy="12" r="12" fill="var(--ink)"/><rect x="8" y="5" width="8" height="14" rx="1.5" fill="#fff"/></svg>
      </li>
      <li>(000) 000-0000
        <svg viewBox="0 0 24 24" aria-label="Phone"><circle cx="12" cy="12" r="12" fill="var(--ink)"/><path d="M6 10 Q12 5 18 10 L16 12 L14 10.5 L10 10.5 L8 12 Z M8 13 H16 L17 18 H7 Z" fill="#fff"/></svg>
      </li>
      <li>name@galaglow.com
        <svg viewBox="0 0 24 24" aria-label="Email"><circle cx="12" cy="12" r="12" fill="var(--ink)"/><rect x="6" y="8" width="12" height="8" fill="#fff"/><path d="M6 8 L12 13 L18 8" fill="none" stroke="var(--ink)" stroke-width="1.3"/></svg>
      </li>
      <li>galaglow.com/team/name
        <svg viewBox="0 0 24 24" aria-label="Profile"><circle cx="12" cy="12" r="12" fill="var(--ink)"/></svg>
      </li>
    </ul>

    <p class="website">www.galaglow.com</p>
  </section>

  <section class="card card--back" aria-label="Business card back">
    <svg class="card__band" viewBox="0 0 945 200" preserveAspectRatio="none" aria-hidden="true">
      <path d="M300 130 C600 120 820 80 945 20 L945 60 C800 110 600 132 300 132 Z" fill="var(--grey)"/>
      <path d="M0 132 C350 132 700 120 945 55 L945 200 L0 200 Z" fill="var(--pink)"/>
    </svg>
    <div class="brand">Gala Glow</div>
  </section>

</main>
</body>
</html>
```